40k Ultra High Pressure Waterblasing Ad

We need 1 page flyer ad for our industry's brochure/membership directory.
We're a manufacturer & supplier for the Ultra High Pressure Waterblasting industry.
We'd like the ad to be simple and clean, highlighting some of our parts. Our dedication to our customers and affordable prices.
Some of the parts are Dorvel Mastrick Hoses, Sapphire Nozzles, Rotating Jetlance.

Our website is torvaflux.com

Requirements
Must have
• Dorvel Mastrick 40k Hose
• Sapphire Nozzles
• Rotating Jetlance
• **Update - Would like to incorporate the "iron skein logo w/ bulldog" from uploaded dorvel iron skein hose attachment. Highlighting the hose's features.
Nice to have
• Brief Bullet points or something else highlighting what we sell.
• - Pump replacement parts
• - Sapphire Nozzles
• - Rotating Jetlance
• - Fittings and adapters
• - Safety Gear
• I've uploaded past ads we've used.
Should not have
• Lots of text area

```html
<!DOCTYPE html>
<html lang="en">
<head>
<meta charset="UTF-8">
<title>40K Ultra High Pressure Waterblasting Flyer</title>
<link href="https://fonts.googleapis.com/css2?family=Anton&family=Fira+Sans:wght@500;600&family=Oswald:wght@500;600&display=swap" rel="stylesheet">
<style>
  :root {
    --brand-blue: #2342a0;
    --navy: #1b3563;
    --ink: #1e1e1e;
    --body-grey: #555a60;
    --page-bg: #e8e8e6;
    --paper: #ffffff;
    --sunset-dark: #5a2a1e;
    --sunset-mid: #c8602e;
    --sunset-light: #f2b04a;
    --steel: #b9bcc0;
    --steel-dark: #7d8186;
  }
  html, body { margin: 0; width: 1200px; height: 1200px; overflow: hidden; background: var(--page-bg); }
  .flyer {
    position: absolute; left: 175px; top: 0; width: 850px; height: 1200px;
    background: var(--paper); overflow: hidden;
  }
  .frame-line { position: absolute; inset: 0; }
  .brand {
    position: absolute; top: 50px; left: 0; width: 850px; text-align: center;
    font-family: "Oswald", sans-serif; font-weight: 600; font-size: 28px; line-height: 40px;
    color: var(--brand-blue); letter-spacing: 1px;
  }
  .brand .mark { display: inline-block; width: 14px; height: 14px; background: var(--brand-blue); margin-right: 8px; vertical-align: 3px; }
  .hose-tip {
    position: absolute; left: 612px; top: 0; width: 44px; height: 118px;
    background: linear-gradient(90deg, var(--steel-dark), #e2e4e6 45%, var(--steel-dark));
    border-radius: 0 0 14px 14px; transform: rotate(16deg); transform-origin: top center;
  }
  .headline {
    position: absolute; left: 190px; top: 100px; margin: 0;
    display: flex; align-items: flex-end; color: var(--brand-blue); font-weight: 400;
  }
  .headline .big { font-family: "Anton", sans-serif; font-size: 140px; line-height: 0.9; letter-spacing: -2px; }
  .headline .stack { font-family: "Anton", sans-serif; font-size: 36px; line-height: 1.05; margin-left: 6px; padding-bottom: 4px; }
  .hero-photo {
    position: absolute; left: 20px; top: 262px; width: 810px; height: 418px;
    background: radial-gradient(circle at 48% 65%, #fff4dc 0, var(--sunset-light) 10%, var(--sunset-mid) 35%, var(--sunset-dark) 80%);
  }
  .nozzle-photo {
    position: absolute; left: 600px; top: 505px; width: 200px; height: 205px;
    background: radial-gradient(circle at 40% 40%, #eceef0, var(--steel) 60%, #8a8e93);
    border-radius: 50%;
  }
  .offerings {
    position: absolute; left: 132px; top: 688px; width: 460px;
    font-family: "Fira Sans", sans-serif; font-weight: 500; font-size: 21px;
    color: var(--body-grey); line-height: 40px; letter-spacing: 0.3px;
  }
  .partner {
    position: absolute; left: 612px; top: 745px;
    font-family: "Oswald", sans-serif; font-weight: 600; font-size: 24px; color: var(--ink);
    display: flex; align-items: center; gap: 8px;
  }
  .partner .dot { width: 28px; height: 28px; border-radius: 50%; background: var(--steel); }
  .product { position: absolute; top: 822px; width: 170px; text-align: center; }
  .product .shot { height: 100px; border: 2px solid var(--navy); padding: 4px; box-sizing: border-box; }
  .product .shot div { width: 100%; height: 100%; }
  .product .caption { margin-top: 16px; font-family: "Oswald", sans-serif; font-weight: 600; font-size: 13px; color: var(--ink); white-space: nowrap; }
  .hose-shot { background: linear-gradient(160deg, #d9dbde, #8f9398 55%, #b4b7bb); }
  .lance-shot { background: linear-gradient(160deg, #e4e5e7, #9a9ea3 50%, #c9cbce); }
  .sapphire-shot { background: linear-gradient(160deg, #e2dfdc, #8e847a 55%, #c2bcb6); }
  .cta { position: absolute; left: 190px; top: 995px; width: 345px; height: 64px; }
  .cta svg { position: absolute; left: 0; top: 0; }
  .cta-text {
    position: absolute; left: 18px; top: 8px; width: 290px; text-align: center;
    font-family: "Fira Sans", sans-serif; font-weight: 600; color: #fff; line-height: 1.1;
  }
  .cta-text .main { font-size: 22px; letter-spacing: 0.5px; }
  .cta-text .sub { font-size: 16px; }
  .phone {
    position: absolute; left: 570px; top: 1008px;
    font-family: "Oswald", sans-serif; font-weight: 600; font-size: 36px; line-height: 44px; color: var(--ink);
  }
  .footer {
    position: absolute; left: 0; top: 1146px; width: 850px; text-align: center;
    font-family: "Fira Sans", sans-serif; font-weight: 600; font-size: 14px;
    color: var(--navy); letter-spacing: 6px;
  }
</style>
</head>
<body>
  <main class="flyer">
    <svg class="frame-line" width="850" height="1200" aria-hidden="true">
      <polyline points="330,72 62,72 62,1122 790,1122 790,72 640,72" fill="none" stroke="#1b3563" stroke-width="3"/>
    </svg>

    <div class="brand"><span class="mark"></span>Torvaflux</div>
    <div class="hose-tip" role="img" aria-label="Photo of a high pressure hose end fitting"></div>

    <h1 class="headline">
      <span class="big">40K</span>
      <span class="stack">ULTRA<br>HIGH PRESSURE<br>WATERBLASING</span>
    </h1>

    <div class="hero-photo" role="img" aria-label="Photo of an offshore oil platform at sunset"></div>
    <div class="nozzle-photo" role="img" aria-label="Photo of two multi-orifice steel nozzle heads"></div>

    <div class="offerings">
      Pump Replacement Parts | Sapphire Nozzles<br>
      Rotating Jetlance | Fittings And Adapters<br>
      Safety Gear
    </div>

    <div class="partner"><span>IRON SKEIN</span><span class="dot"></span></div>

    <div class="product" style="left:110px">
      <div class="shot"><div class="hose-shot" role="img" aria-label="Photo of a coiled 40K hose"></div></div>
      <div class="caption">DORVEL MASTRICK 40K HOSE</div>
    </div>
    <div class="product" style="left:340px">
      <div class="shot"><div class="lance-shot" role="img" aria-label="Photo of a rotating jetlance tool"></div></div>
      <div class="caption">ROTATING JETLANCE</div>
    </div>
    <div class="product" style="left:570px">
      <div class="shot"><div class="sapphire-shot" role="img" aria-label="Photo of sapphire nozzle inserts"></div></div>
      <div class="caption">SAPPHIRE NOZZLES</div>
    </div>

    <div class="cta">
      <svg width="345" height="64" aria-hidden="true"><polygon points="0,0 315,0 345,32 315,64 0,64" fill="#1b3563"/></svg>
      <div class="cta-text"><div class="main">AT AFFORDABLE PRICES</div><div class="sub">CALL US TODAY</div></div>
    </div>
    <div class="phone">555-014-2270</div>

    <div class="footer">info@torvaflux.com &nbsp;| &nbsp;www.torvaflux.com</div>
  </main>
</body>
</html>
```